Bramble Nook

I need a vinyl banner for my tent when I do Festivals both outside and inside. The banner will be approximately 3 feet high and 5 feet long.
I will be selling vintage and antique items mainly smalls not large furniture. See pictures for the types of items I will be selling. Also vintage bar ware, VOLAX, Glassware, Dresmel Ware, ect.

```html
<!DOCTYPE html>
<html lang="en">
<head>
<meta charset="utf-8">
<title>Bramble Nook – Tent Banner</title>
<link rel="stylesheet" href="https://fonts.googleapis.com/css2?family=Oranienbaum&family=Cinzel:wght@500&family=Pathway+Gothic+One&display=swap">
<style>
  :root {
    --page: #a3a3a3;
    --cream: #efe6d1;
    --cream-edge: #e3d6ba;
    --rust: #8e3a21;
    --navy: #26344c;
    --ribbon: #213a5c;
    --ribbon-dark: #18293f;
    --ribbon-text: #f1ead9;
  }
  * { margin: 0; padding: 0; box-sizing: border-box; }
  html, body { width: 1057px; height: 1200px; overflow: hidden; background: var(--page); }
  .banner {
    position: absolute; left: 28px; top: 300px;
    width: 1000px; height: 600px;
    background: radial-gradient(ellipse at center, var(--cream) 55%, var(--cream-edge) 100%);
    box-shadow: 0 18px 40px rgba(0,0,0,.35);
    color: var(--navy);
  }
  .banner-frame { position: absolute; inset: 0; }
  .ornament {
    position: absolute; left: 50%; transform: translateX(-50%);
    background: var(--navy); opacity: .25; border-radius: 20px;
  }
  .ornament--crest { top: 42px; width: 200px; height: 34px; }
  .ornament--divider { top: 266px; width: 50px; height: 14px; }
  .ornament--lower { top: 506px; width: 40px; height: 9px; background: var(--rust); }
  .ornament--foot { top: 552px; width: 30px; height: 10px; background: var(--rust); }
  .title {
    position: absolute; top: 92px; width: 100%; text-align: center;
    font-family: "Oranienbaum", serif; font-size: 116px; line-height: 1;
    color: var(--rust); font-weight: 400;
  }
  .subtitle {
    position: absolute; top: 214px; width: 100%; text-align: center;
    font-family: "Cinzel", serif; font-weight: 500; font-size: 42px; line-height: 1;
    color: var(--navy);
  }
  .rule { position: absolute; height: 2px; background: var(--navy); }
  .rule--sub-left { left: 75px; width: 75px; top: 237px; }
  .rule--sub-right { left: 850px; width: 75px; top: 237px; }
  .rule--divider-left { left: 187px; width: 285px; top: 272px; height: 1.5px; }
  .rule--divider-right { left: 528px; width: 285px; top: 272px; height: 1.5px; }
  .categories {
    position: absolute; top: 294px; left: 190px; width: 620px; text-align: center;
    font-family: "Pathway Gothic One", sans-serif; font-size: 48px; line-height: 1;
    color: var(--rust); white-space: nowrap;
  }
  .ribbon { position: absolute; left: 247px; top: 370px; width: 497px; height: 108px; }
  .ribbon-text {
    position: absolute; left: 247px; top: 386px; width: 497px; text-align: center;
    font-family: "Pathway Gothic One", sans-serif; font-size: 34px; line-height: 31px;
    color: var(--ribbon-text);
  }
  .tagline {
    position: absolute; top: 520px; left: 270px; width: 460px; text-align: center;
    font-family: "Pathway Gothic One", sans-serif; font-size: 22px; line-height: 1;
    color: var(--navy); white-space: nowrap;
  }
  .photo { position: absolute; border-radius: 10px; }
  .photo--lamp {
    left: 24px; top: 276px; width: 140px; height: 236px;
    background: linear-gradient(180deg, #e2e2e2 0%, #c9c9c9 60%, #b5b5b5 100%);
  }
  .photo--tableware {
    left: 164px; top: 360px; width: 80px; height: 160px;
    background: linear-gradient(160deg, #b9a67a 0%, #a08040 55%, #8e1f22 100%);
  }
  .photo--flowers {
    left: 826px; top: 304px; width: 120px; height: 52px;
    background: linear-gradient(180deg, #c59a5a 0%, #a98552 100%);
  }
  .photo--crates {
    left: 748px; top: 356px; width: 238px; height: 166px;
    background: linear-gradient(200deg, #8c8c7a 0%, #8a4a25 50%, #1f4a3a 100%);
  }
</style>
</head>
<body>
  <section class="banner">
    <svg class="banner-frame" width="1000" height="600" viewBox="0 0 1000 600" aria-hidden="true">
      <path d="M31 11 H969 A20 20 0 0 0 989 31 V569 A20 20 0 0 0 969 589 H31 A20 20 0 0 0 11 569 V31 A20 20 0 0 0 31 11 Z"
            fill="none" stroke="var(--navy)" stroke-width="4"/>
      <path d="M38 20 H962 A18 18 0 0 0 980 38 V562 A18 18 0 0 0 962 580 H38 A18 18 0 0 0 20 562 V38 A18 18 0 0 0 38 20 Z"
            fill="none" stroke="var(--navy)" stroke-width="1.5"/>
    </svg>

    <div class="ornament ornament--crest" role="img" aria-label="Fleur-de-lis scroll ornament"></div>
    <h1 class="title">BRAMBLE NOOK</h1>

    <span class="rule rule--sub-left"></span>
    <h2 class="subtitle">VINTAGE AND ANTIQUE FINDS</h2>
    <span class="rule rule--sub-right"></span>

    <span class="rule rule--divider-left"></span>
    <div class="ornament ornament--divider" role="img" aria-label="Small scroll divider ornament"></div>
    <span class="rule rule--divider-right"></span>

    <p class="categories">Antiques . Smalls . Barware . Collectibles</p>

    <div class="photo photo--lamp" role="img" aria-label="Photo of a clear glass oil lamp with frilled shade"></div>
    <div class="photo photo--tableware" role="img" aria-label="Photo of a chrome teapot, brass mantel clock and red glass tumblers"></div>
    <div class="photo photo--flowers" role="img" aria-label="Photo of a dried flower arrangement in a woven pot"></div>
    <div class="photo photo--crates" role="img" aria-label="Photo of a metal basket, wooden seed crate and painted green tin box"></div>

    <svg class="ribbon" width="497" height="108" viewBox="0 0 497 108" aria-hidden="true">
      <path d="M28 0 H469 L497 54 L469 108 H28 L0 54 Z" fill="var(--ribbon-dark)"/>
      <path d="M34 6 H463 L488 54 L463 102 H34 L9 54 Z" fill="var(--ribbon)" stroke="var(--ribbon-text)" stroke-opacity=".35" stroke-width="1"/>
    </svg>
    <p class="ribbon-text">VOLAX · Glassware · Dresmel Ware ·<br>Kitchenware . Unique Home Décor</p>

    <div class="ornament ornament--lower" role="img" aria-label="Small scroll ornament"></div>
    <p class="tagline">One-of-a-kind finds for collectors, decorators &amp; treasure hunters</p>
    <div class="ornament ornament--foot" role="img" aria-label="Small flourish ornament"></div>
  </section>
</body>
</html>
```